Revamp our wedding venue website

Currently we are using wordpress for our website and hoped to find a designer that can assist us with making the website prettier and more pleasing and draw more interest. www.velmorhall.net is our current site. We are connected to google business mail, so I would prefer to stay with this for now and update our gallery with new photos, blog page and putting the contact us form back on all the pages.

Target Market(s)

20-40 years of age, all ranges of styles and generally clients looking for a different modern feel vs. a hotel hall.

Industry/Entity Type

Wedding

Logo Text

1947 Velmor Hall

Number of Pages Required

4 page

Font styles to use
Serif

Requirements
Must have
• Light, airy feel. Romantic and informative. Mobile friendly and easy to contact us-preferred contact form on all pages. Gallery of photos. Previous reviews
Nice to have
• Bio of staff, maybe some videos, and fun things to do in the area for out of town guests. Maps and also venue blank floor plan.

```html
<!DOCTYPE html>
<html lang="en">
<head>
<meta charset="utf-8">
<title>1947 Velmor Hall — Weddings &amp; Events</title>
<link rel="stylesheet" href="https://fonts.googleapis.com/css2?family=Great+Vibes&family=Roboto:wght@400;500&family=Roboto+Slab:wght@400&display=swap">
<style>
:root{
  --coral:#e85a4f;
  --coral-deep:#d9473f;
  --ink:#4a4a4a;
  --muted:#777;
  --rule:#c9c9c9;
  --gold:#f5b800;
  --white:#fff;
  --sky:#7dc8e0;
  --rose:#f08a86;
  --navy:#5b6fb3;
  --sun:#f3cf67;
}
*{box-sizing:border-box;margin:0;padding:0}
html,body{width:1200px;height:2479px;overflow:hidden;background:var(--white)}
body{position:relative;font-family:"Roboto",Arial,sans-serif;color:var(--ink)}
.abs{position:absolute}
.script{font-family:"Great Vibes",cursive;font-weight:400}

/* nav */
.main-nav{top:0;left:0;width:1200px;height:76px;display:flex;justify-content:center;align-items:center}
.main-nav a{position:absolute;top:29px;font-size:14px;color:#555;text-decoration:none;text-transform:uppercase;letter-spacing:.3px}
.main-nav a.is-active{color:var(--coral)}

/* brand band */
.brand-band{top:76px;left:0;width:1200px;height:96px;background:var(--coral)}
.brand-band .brand-name{position:absolute;top:26px;width:100%;text-align:center;color:var(--white);font-size:26px;font-family:"Roboto",Arial,sans-serif;letter-spacing:1px}
.brand-band .stitch{position:absolute;left:0;right:0;top:158px;border-top:1px dashed rgba(255,255,255,.8)}

/* hero */
.hero{top:172px;left:0;width:1200px;height:534px;background:linear-gradient(100deg,#3a2a22 0%,#8a6f5c 30%,#efe6da 50%,#8f7866 72%,#2e231d 100%)}
.slider-dots{top:671px;left:555px;display:flex;gap:11px}
.slider-dots span{width:14px;height:14px;border:2px solid var(--white);border-radius:50%}
.slider-dots span.is-current{background:var(--coral);border-color:var(--white)}

/* welcome */
.welcome{top:740px;left:99px;width:460px}
.welcome .script{font-size:34px;color:#333}
.welcome .underline{width:66px;height:2px;background:var(--coral);margin:2px 0 6px}
.section-sub{font-size:18px;color:#444;margin-bottom:10px}
.body-copy{font-size:12px;line-height:18.6px;color:var(--muted);margin-bottom:12px}
.btn{display:inline-block;background:var(--coral);color:var(--white);font-size:12px;font-weight:500;text-transform:uppercase;padding:11px 12px;text-decoration:none;letter-spacing:.3px}
.welcome .btn{position:absolute;top:315px;left:0;width:98px;text-align:center}
.welcome-photo{top:752px;left:600px;width:501px;height:339px;border:1px solid #ddd;padding:3px;background:var(--white)}
.welcome-photo div{width:100%;height:100%;background:linear-gradient(110deg,#f4f1ec 0%,#e4ddd3 45%,#b9c2cf 70%,#e9d6d6 100%)}

.dotted{left:0;width:1200px;border-top:2px dotted var(--rule)}

/* offer */
.offer{top:1159px;left:0;width:1200px;height:567px;background:radial-gradient(ellipse at 30% 40%,#f08c80 0%,#e4675b 45%,#cf4a40 100%)}
.offer .script{position:absolute;top:28px;width:100%;text-align:center;color:var(--white);font-size:34px}
.offer .tagline{position:absolute;top:64px;width:100%;text-align:center;color:var(--white);font-size:25px}
.offer-video{top:1294px;left:260px;width:681px;height:374px;border:3px solid var(--white);background:linear-gradient(120deg,#3b3a35 0%,#8e8a7c 45%,#d7d2c4 60%,#5d564a 100%)}
.play{position:absolute;left:306px;top:153px}

/* useful info */
.useful{top:1792px;left:99px;width:330px}
.useful .script,.events .script{font-size:34px;color:#333}
.useful .section-sub{margin-top:4px;margin-bottom:14px}
.info-list{list-style:none;margin-top:16px}
.info-list li{position:relative;padding-left:18px;font-size:12px;text-transform:uppercase;color:#444;height:27.5px;line-height:18px}
.info-list li::before{content:"";position:absolute;left:1px;top:5px;width:6px;height:6px;border-top:2px solid var(--coral);border-right:2px solid var(--coral);transform:rotate(45deg)}
.useful .btn{margin-top:19px;width:98px;text-align:center}

/* events */
.events{top:1792px;left:474px;width:628px}
.event-card{position:absolute;left:0;width:628px;height:150px}
.event-photo{position:absolute;left:-3px;top:0;width:220px;height:149px}
.event-photo.one{background:linear-gradient(120deg,#3c342c 0%,#9aa38a 45%,#e9e6df 70%,#cfc7bb 100%)}
.event-photo.two{background:linear-gradient(120deg,#c4d7e6 0%,#f1f3f6 45%,#c9b0bd 70%,#5a6477 100%)}
.event-body{position:absolute;left:242px;top:0;width:386px}
.event-title{font-size:18px;color:#444;margin-top:-2px}
.stars{color:var(--gold);font-size:14px;letter-spacing:1px;margin-top:3px;line-height:18px}
.stars .off{color:#d9d9d9}
.meta{font-size:10px;color:#666;margin-top:2px}
.meta .count{color:var(--coral)}
.event-copy{font-size:11px;line-height:19px;color:var(--muted);margin-top:7px;text-align:justify}
.event-divider{position:absolute;left:0;top:221px;width:625px;border-top:2px dotted var(--rule)}
.more-events{top:2193px;left:1071px;width:30px;height:30px;border-radius:50%;background:var(--gold)}

/* footer */
.footer-links{top:2306px;left:0;width:1200px;text-align:center;font-family:"Roboto Slab",Georgia,serif;font-size:14px;color:#444}
.footer-links span.sep{margin:0 17px;color:#666}
.social{top:2355px;left:496px;display:flex;gap:14px}
.social span{width:40px;height:40px;border-radius:50%}
.legal{top:2421px;left:381px;font-size:11px;color:#555;display:flex;gap:22px}
.bottom-bar{top:2473px;left:0;width:1200px;height:6px;background:var(--coral)}
</style>
</head>
<body>

<nav class="main-nav abs">
  <a class="is-active" style="left:271px">Home</a>
  <a style="left:367px">Weddings</a>
  <a style="left:494px">Events</a>
  <a style="left:603px">Catering</a>
  <a style="left:726px">Gallery</a>
  <a style="left:843px">Contact Us</a>
</nav>

<header class="brand-band abs">
  <div class="brand-name">1947 Velmor Hall</div>
</header>
<div class="abs" style="left:0;top:158px;width:1200px;border-top:1px dashed rgba(255,255,255,.85)"></div>

<section class="hero abs" role="img" aria-label="Bride and groom embracing on an ornate marble staircase"></section>
<div class="slider-dots abs"><span></span><span class="is-current"></span><span></span><span></span></div>

<section class="welcome abs">
  <h2 class="script">Welcome!</h2>
  <div class="underline"></div>
  <h3 class="section-sub">Weddings &amp; Events at the 1947 Velmor Hall</h3>
  <p class="body-copy">When choosing the location for your wedding or event, the 1947 Velmor Hall provides you with an all-inclusive experience, from the moment you arrive, through the creative food, and amazing photo opportunities. The unique open-kitchen provides you, and your guests a front-row seat to our creative, and talented chefs, as they prepare a culinary experience like no other. The full, and spacious bar, serves up wonderful libations and specialty cocktails that enhance your experience.</p>
  <p class="body-copy">Watch this short video to find out more about having your event here at the 1947 Velmor Hall. Then, look around the site, check out the photos, and then call or contact our wedding and event specialists today, to check date availability, and to arrange your personal tour of the 1947 Velmor Hall, 555.214.0947, Events@VelmorHall.net</p>
  <a class="btn">Learn More</a>
</section>
<figure class="welcome-photo abs"><div role="img" aria-label="Couple sharing a moment beside a white balustrade under falling petals"></div></figure>

<div class="dotted abs" style="top:1128px"></div>

<section class="offer abs" role="img" aria-label="Soft-focus wedding guests celebrating in warm coral light">
  <h2 class="script">Hot Offer</h2>
  <p class="tagline">for your best day!</p>
</section>
<div class="offer-video abs" role="img" aria-label="Video still of newlyweds kissing as guests throw confetti">
  <svg class="play" width="64" height="64" viewBox="0 0 64 64"><circle cx="32" cy="32" r="29" fill="none" stroke="#fff" stroke-width="3"/><path d="M25 19 L46 32 L25 45 Z" fill="#fff"/></svg>
</div>

<div class="dotted abs" style="top:1759px"></div>

<section class="useful abs">
  <h2 class="script">Useful Info</h2>
  <h3 class="section-sub">Bertasad serasaset mias metase vetrasas</h3>
  <p class="body-copy">Want to find out more about having your wedding or event here at the beautiful, historic 1947 Velmor Hall, call or contact our wedding and event specialists today,</p>
  <ul class="info-list">
    <li>Wedding Top Tens</li>
    <li>Cakes</li>
    <li>Wedding Planning</li>
    <li>Bridal Accessories</li>
    <li>Photo Studio</li>
    <li>Flowers</li>
    <li>Decorations</li>
  </ul>
  <a class="btn">Learn More</a>
</section>

<section class="events abs">
  <h2 class="script">Our Events</h2>
  <article class="event-card" style="top:53px">
    <div class="event-photo one" role="img" aria-label="Bride and groom holding hands outdoors"></div>
    <div class="event-body">
      <h3 class="event-title">Events at the 1947 Velmor Hall</h3>
      <div class="stars">★★★<span class="off">★★</span></div>
      <div class="meta"><span class="count">66 Reviews</span> • Write a Review &nbsp; Larkport, FL</div>
      <p class="event-copy">We cater to a variety of events, such as, Weddings, Rehearsal Dinners, Fashion Shows, Anniversary parties, Bar/Bat Mitzvah's, Corporate Meetings/Seminars, and Fundraisers. Our staff goes above and beyond to assist you with decoration</p>
    </div>
  </article>
  <div class="event-divider"></div>
  <article class="event-card" style="top:245px">
    <div class="event-photo two" role="img" aria-label="Smiling newlyweds with a bouquet"></div>
    <div class="event-body">
      <h3 class="event-title">Events at the 1947 Velmor Hall</h3>
      <div class="stars">★★★<span class="off">★★</span></div>
      <div class="meta"><span class="count">66 Reviews</span> • Write a Review &nbsp; Larkport, FL</div>
      <p class="event-copy">We cater to a variety of events, such as, Weddings, Rehearsal Dinners, Fashion Shows, Anniversary parties, Bar/Bat Mitzvah's, Corporate Meetings/Seminars, and Fundraisers. Our staff goes above and beyond to assist you with decoration</p>
    </div>
  </article>
</section>
<svg class="more-events abs" viewBox="0 0 30 30" aria-label="More events"><circle cx="15" cy="15" r="15" fill="#f5b800"/><path d="M10 10 L14 15 L10 20 M15 10 L19 15 L15 20" fill="none" stroke="#fff" stroke-width="2"/></svg>

<div class="dotted abs" style="top:2257px"></div>

<footer>
  <nav class="footer-links abs">Home<span class="sep">|</span>Weddings<span class="sep">|</span>Events<span class="sep">|</span>Catering<span class="sep">|</span>Gallery<span class="sep">|</span>Contact Us</nav>
  <div class="social abs" aria-label="Social links">
    <span style="background:var(--sky)"></span>
    <span style="background:var(--rose)"></span>
    <span style="background:var(--navy)"></span>
    <span style="background:var(--sun)"></span>
  </div>
  <div class="legal abs"><span>Are You A Vendor?</span><span>Terms &amp; Privacy</span><span>Help</span><span>© 2006-2016 Vowline, Inc.</span></div>
  <div class="bottom-bar abs"></div>
</footer>

</body>
</html>
```